Brookfield Animal Care Partners of Central Pennsylvania

I need a business card design for a new company in Harrisburg PA called "Animal Care Partners of Brookfield Central PA". I will be providing relief services for veterinarians who need coverage during vacations; sick/maternity leave, etc. I would like to see the veterinarian symbol incorporated in the design in combination with animals (dogs /cats/birds/reptiles an pocket pets). Include My full name: Tomás R. Quintela DVM, MLAS, BS. Also include my e mail (dvmtrq@mailnest.example) and phone number 5550184627

Target Market(s)

Small Animal Veterinarian, practice owner

Industry/Entity Type

Business

Contact Information for Business Card

Brookfield Animal Care Partners of Central PA

Font styles to use
Script

Requirements
Must have
• Veterinarian caduceus (see image) and Small animals (pets) within the logo.
Nice to have
• Give a sense of relaxation (vacationing)
Should not have
• Large animals, i.e. horses, cows, zoo animals...

```html
<!DOCTYPE html>
<html lang="en">
<head>
<meta charset="utf-8">
<title>Brookfield Animal Care Partners – Business Card</title>
<link rel="stylesheet" href="https://fonts.googleapis.com/css2?family=Cinzel:wght@700&family=Dancing+Script:wght@700&family=Raleway:wght@500&display=swap">
<style>
  :root {
    --backdrop: #1c1c1c;
    --card-dark: #2c2c2c;
    --card-light: #404040;
    --accent-blue: #2a9ad8;
    --ink: #0e0e0e;
  }
  html, body {
    margin: 0;
    width: 1200px;
    height: 902px;
    overflow: hidden;
    background: var(--backdrop);
  }
  .business-card {
    position: absolute;
    left: 80px;
    top: 154px;
    width: 1040px;
    height: 593px;
    border-radius: 26px;
    overflow: hidden;
    box-shadow: 0 0 0 1px rgba(255,255,255,0.08);
  }
  .business-card svg { display: block; width: 100%; height: 100%; }
  .company-name {
    font-family: "Cinzel", serif;
    font-weight: 700;
    font-size: 24px;
    fill: var(--accent-blue);
    letter-spacing: 0.5px;
  }
  .logo-name {
    font-family: "Cinzel", serif;
    font-weight: 700;
    font-size: 24px;
    fill: var(--accent-blue);
  }
  .person-name {
    font-family: "Dancing Script", cursive;
    font-weight: 700;
    font-size: 52px;
    fill: var(--accent-blue);
  }
  .credentials {
    font-family: "Raleway", sans-serif;
    font-weight: 500;
    font-size: 24px;
    fill: var(--ink);
    letter-spacing: 2px;
  }
  .contact-line {
    font-family: "Raleway", sans-serif;
    font-weight: 500;
    font-size: 26px;
    fill: var(--ink);
    letter-spacing: 1px;
  }
</style>
</head>
<body>
  <div class="business-card">
    <svg viewBox="0 0 938 535" xmlns="http://www.w3.org/2000/svg">
      <defs>
        <linearGradient id="card-surface" x1="0" y1="0" x2="1" y2="0">
          <stop offset="0" stop-color="var(--card-dark)"/>
          <stop offset="1" stop-color="var(--card-light)"/>
        </linearGradient>
      </defs>
      <rect class="card-surface" width="938" height="535" fill="url(#card-surface)"/>

      <!-- accent crescent band -->
      <path class="accent-band" fill="var(--accent-blue)" fill-rule="evenodd"
        d="M57 -156 a423 423 0 1 1 0 846 a423 423 0 1 1 0 -846 Z
           M125.5 -57.5 a324.5 324.5 0 1 0 0 649 a324.5 324.5 0 1 0 0 -649 Z"/>

      <!-- brand mark -->
      <g class="brand-mark">
        <circle cx="210" cy="275" r="132" fill="none" stroke="var(--accent-blue)" stroke-width="14"/>
        <text class="logo-name" x="210" text-anchor="middle">
          <tspan x="210" y="252">Brookfield</tspan>
          <tspan x="210" y="284">Animal Care</tspan>
          <tspan x="210" y="316">Partners</tspan>
        </text>
      </g>

      <!-- company name -->
      <text class="company-name" text-anchor="middle">
        <tspan x="698" y="100">Brookfield Animal Care Partners</tspan>
        <tspan x="698" y="125">of</tspan>
        <tspan x="698" y="150">Central Pennsylvania</tspan>
      </text>

      <text class="person-name" x="698" y="260" text-anchor="middle">Tomás R. Quintela</text>
      <text class="credentials" x="698" y="292" text-anchor="middle">DVM, MLAS, BS</text>

      <text class="contact-line" x="698" y="402" text-anchor="middle">5550184627</text>
      <text class="contact-line" x="698" y="436" text-anchor="middle">dvmtrq@mailnest.example</text>
    </svg>
  </div>
</body>
</html>
```